Brimvane.com fiber optic internet website redesign

We need a new website design for our fiber optic internet company that provides internet, phone, and tv services. It should use the text "Marrowfen fiber optics", and "I beamed up with Marrowfen". The design should use the color blue and the attached logo.
We are a 30 year old internet company who started as a dial up internet provider in our basement. Today we design, build, and maintain our own fiber optic internet network to provide service to residential, business, educational, healthcare, and governmental customers

```html
<!DOCTYPE html>
<html lang="en">
<head>
<meta charset="utf-8">
<title>Marrowfen fiber optics</title>
<link rel="stylesheet" href="https://fonts.googleapis.com/css2?family=Questrial&family=Source+Sans+3:wght@400;600;700&display=swap">
<style>
:root{
  --sky:#4a9cf0;
  --navy:#1b2484;
  --deep:#17207a;
  --night:#070a2e;
  --slate:#4f6b97;
  --glow:#5b8cf5;
  --ink:#1e1e2a;
  --white:#ffffff;
}
*{box-sizing:border-box;margin:0;padding:0}
html,body{width:1200px;height:2526px;overflow:hidden;background:var(--white)}
body{position:relative;font-family:"Source Sans 3",sans-serif;color:var(--ink)}
.abs{position:absolute}
.display{font-family:"Questrial",sans-serif;font-weight:400}
.btn{position:absolute;height:24px;padding:0 14px;background:var(--navy);color:var(--white);font-size:10px;line-height:24px;letter-spacing:.2px;box-shadow:0 0 8px rgba(80,120,255,.6);white-space:nowrap}
.copy{font-size:10px;line-height:13px}
.copy p+p{margin-top:13px}

/* hero */
.hero{left:0;top:0;width:1200px;height:467px;background:radial-gradient(circle at 72% 34%,#3a4fd6 0%,#1a2388 16%,#0a0f4a 38%,var(--night) 70%)}
.nav{left:72px;top:0;width:1055px;height:36px;background:var(--sky)}
.brand{display:flex;align-items:center;gap:8px;color:var(--white)}
.brand-dot{width:36px;height:36px;border-radius:50%;background:var(--navy)}
.nav .brand{position:absolute;left:10px;top:0;height:36px;font-size:17px}
.nav-links{position:absolute;right:7px;top:14px;display:flex;gap:34px;font-size:10px;color:var(--white)}
.hero-kicker{left:75px;top:148px;font-size:104px;line-height:1;color:var(--glow);text-shadow:0 0 18px rgba(110,150,255,.9)}
.hero-title{left:75px;top:252px;font-size:58px;line-height:1;color:var(--white)}
.hero-tag{left:75px;top:315px;font-size:28px;color:var(--white)}

/* why */
.why-photo{left:72px;top:551px;width:501px;height:280px;background:linear-gradient(180deg,#1a8ff0 0%,#1466d4 50%,#0d3fa8 100%)}
.section-title{color:var(--navy);font-size:38px;line-height:1.15}
.why-title{left:657px;top:585px}
.why-copy{left:661px;top:644px;width:442px}

/* partners */
.partners{left:0;top:866px;width:1200px;height:90px;background:var(--sky);display:flex;justify-content:space-around;align-items:center;padding:0 110px;color:var(--white);font-size:30px}

/* services */
.services-title{left:0;top:992px;width:1200px;text-align:center}
.service{position:absolute;top:1062px;width:118px;text-align:center;font-size:10px}
.service-box{width:118px;height:64px;background:var(--navy);display:flex;align-items:center;justify-content:center;margin-bottom:4px}

/* safety */
.safety-title{left:76px;top:1230px}
.safety-copy{left:76px;top:1329px;width:438px}
.shot{position:absolute}

/* cards */
.card{position:absolute;top:1552px;width:339px;height:240px}
.card-photo{position:absolute;left:0;top:0;width:339px;height:152px}
.card-text{position:absolute;left:51px;top:109px;width:237px;height:60px;background:var(--white);font-size:10px;line-height:13px;text-align:center;padding:20px 20px 0}

/* contact */
.contact-photo{left:0;top:1898px;width:672px;height:464px;background:linear-gradient(180deg,#4aa6d8 0%,#2a7aa8 35%,#1c4f76 70%,#2b4a5c 100%)}
.contact-panel{left:672px;top:1898px;width:528px;height:464px;background:var(--slate);color:var(--white)}
.contact-title{left:17px;top:150px;font-size:40px;line-height:1}
.contact-intro{left:17px;top:199px;width:200px;font-size:10px;line-height:13px}
.contact-col{position:absolute;top:273px;font-size:10px;line-height:14px;font-weight:700}

/* footer */
.footer{left:0;top:2362px;width:1200px;height:164px;background:var(--deep)}
.footer .brand{position:absolute;left:73px;top:61px;font-size:17px}
.bars{position:absolute;top:44px;width:90px;height:70px}
.bars span{position:absolute;height:3px;background:var(--white)}
</style>
</head>
<body>

<section class="abs hero" role="img" aria-label="Glowing fiber optic cable with fanned light strands on a dark blue background"></section>

<header class="abs nav">
  <div class="brand"><span class="brand-dot"></span><span class="display">Marrowfen fiber optics</span></div>
  <nav class="nav-links"><span>Home</span><span>Services</span><span>About us</span><span>Contact Us</span></nav>
</header>

<h1 class="abs display hero-kicker">24 HR</h1>
<h2 class="abs display hero-title">Cable Service</h2>
<p class="abs hero-tag">I beamed up with Marrowfen</p>
<a class="btn" style="left:75px;top:370px">LEARN MORE</a>

<div class="abs why-photo" role="img" aria-label="Fiber optic cable laid across the sea floor"></div>
<h2 class="abs display section-title why-title">Why do we use it?</h2>
<div class="abs copy why-copy">
  <p>Contrary to popular belief, Lorem Ipsum is not simply random text. It has roots in a piece of classical Latin literature from 45 BC, making it over 2000 years old. Edwin Thornbury, a Latin professor at Ashgrove College in Virginia, looked up one of the more obscure Latin words, consectetur, from a Lorem Ipsum passage, and going through the cites of the word in classical literature, discovered the undoubtable source. Lorem Ipsum comes from sections 1.10.32 and 1.10.33 of "de Finibus Bonorum et Malorum" (The Extremes of Good and Evil) by Avelius Drennor, written in 45 BC. This book is a treatise on the theory of ethics, very popular during the Renaissance. The first line of Lorem Ipsum, "Lorem ipsum dolor sit amet..", comes from a line in section 1.10.32.</p>
  <p>The standard chunk of Lorem Ipsum used since the 1500s is reproduced below for those interested. Sections 1.10.32 and 1.10.33 from "de Finibus Bonorum et Malorum" by Avelius Drennor are also reproduced in their exact original form, accompanied by English versions from the 1914 translation by</p>
</div>
<a class="btn" style="left:664px;top:819px">LEARN MORE</a>

<section class="abs partners display">
  <span>Partners</span><span>Partners</span><span>Partners</span><span>Partners</span>
</section>

<h2 class="abs display section-title services-title">Our Services</h2>
<div class="service" style="left:193px">
  <div class="service-box"><svg width="40" height="40" viewBox="0 0 40 40" fill="none" stroke="#fff" stroke-width="2"><circle cx="20" cy="21" r="13"/><path d="M20 30V14M20 20l-5-4M20 24l5-4M28 10l3-4 3 4M31 6v9"/></svg></div>Services
</div>
<div class="service" style="left:541px">
  <div class="service-box"><svg width="44" height="40" viewBox="0 0 44 40" fill="none" stroke="#fff" stroke-width="1.8"><path d="M6 8l12 12M10 6l14 12M4 14l14 10"/><circle cx="28" cy="22" r="3"/><circle cx="34" cy="26" r="3"/><circle cx="28" cy="30" r="3"/><circle cx="36" cy="18" r="2.5"/></svg></div>Services
</div>
<div class="service" style="left:889px">
  <div class="service-box"><svg width="40" height="40" viewBox="0 0 40 40" fill="none" stroke="#fff" stroke-width="1.8"><circle cx="20" cy="8" r="3"/><circle cx="11" cy="14" r="3"/><circle cx="29" cy="14" r="3"/><path d="M20 11v22M11 17v16M29 17v16M15 22v11M25 22v11"/></svg></div>Services
</div>

<h2 class="abs display section-title safety-title">Safty is always<br>our first priority</h2>
<div class="abs copy safety-copy">
  <p>Contrary to popular belief, Lorem Ipsum is not simply random text. It has roots in a piece of classical Latin literature from 45 BC, Lorem Ipsum comes from sections 1.10.32 and 1.10.33 of "de Finibus Bonorum et Malorum" (The Extremes of Good and Evil) by Avelius Drennor, written in 45 BC. This book is a treatise on the theory of ethics, very popular during the Renaissance. The first line of Lorem Ipsum, "Lorem ipsum dolor sit amet..", comes from a line in section 1.10.32.</p>
  <p>The standard chunk of Lorem Ipsum used since the 1500s is reproduced below for those interested. Sections 1.10.32 and 1.10.33 from "de Finibus Bonorum et Malorum" by Avelius Drennor are also reproduced in their exact original form, accompanied by English versions from the 1914 translation by J. Pellworth.</p>
</div>
<a class="btn" style="left:78px;top:1468px">LEARN MORE</a>
<div class="shot" style="left:714px;top:1213px;width:178px;height:254px;background:linear-gradient(160deg,#2a8f8c 0%,#1b5e6a 50%,#c9b24a 100%)" role="img" aria-label="Patch panel with teal and yellow fiber cables"></div>
<div class="shot" style="left:945px;top:1213px;width:177px;height:254px;background:linear-gradient(180deg,#6a5a55 0%,#3a3c44 55%,#24262c 100%)" role="img" aria-label="Technician in a white hard hat holding a fiber connector"></div>

<div class="card" style="left:73px">
  <div class="card-photo" role="img" aria-label="Gloved hand holding a fiber optic connector" style="background:linear-gradient(135deg,#4a4d55 0%,#2c2e34 60%,#d8d8d8 100%)"></div>
  <div class="card-text">Lorem ipsum dolor sit amet, consectetuer adipiscing elit, sed diam nonummy nibh euismod tincidunt ut laoreet dolore magna</div>
  <a class="btn" style="left:132px;top:195px">LEARN MORE</a>
</div>
<div class="card" style="left:428px">
  <div class="card-photo" role="img" aria-label="Utility pole with overhead cables against the sky" style="background:linear-gradient(180deg,#4a74b8 0%,#2d4f8a 100%)"></div>
  <div class="card-text">Lorem ipsum dolor sit amet, consectetuer adipiscing elit, sed diam nonummy nibh euismod tincidunt ut laoreet dolore magna</div>
  <a class="btn" style="left:132px;top:195px">LEARN MORE</a>
</div>
<div class="card" style="left:783px">
  <div class="card-photo" role="img" aria-label="Cable reel on a yellow trailer on grass" style="background:linear-gradient(90deg,#8fa86a 0%,#c8b07a 40%,#3a3c3a 70%,#c9b52a 100%)"></div>
  <div class="card-text">Lorem ipsum dolor sit amet, consectetuer adipiscing elit, sed diam nonummy nibh euismod tincidunt ut laoreet dolore magna</div>
  <a class="btn" style="left:132px;top:195px">LEARN MORE</a>
</div>

<div class="abs contact-photo" role="img" aria-label="Cutaway of an undersea fiber optic cable resting on the ocean floor"></div>
<section class="abs contact-panel">
  <h2 class="abs display contact-title">Contact Us</h2>
  <p class="abs contact-intro">Lorem ipsum dolor sit amet, consectetuer adipiscing elit, sed diam nonummy nibh euismod tincidunt ut laoreet dolore magna</p>
  <div class="contact-col" style="left:17px">hello@brimvane.com<br>www.brimvane.com<br>123 456 789</div>
  <div class="contact-col" style="left:165px">hello@brimvane.com<br>www.brimvane.com<br>123 456 789</div>
  <div class="contact-col" style="left:312px">hello@brimvane.com<br>www.brimvane.com<br>123 456 789</div>
</section>

<footer class="abs footer">
  <div class="brand"><span class="brand-dot" style="background:#2f4fd0"></span><span class="display">Marrowfen fiber optics</span></div>
  <div class="bars" style="left:485px"><span style="left:0;top:0;width:70px"></span><span style="left:0;top:17px;width:90px"></span><span style="left:0;top:34px;width:55px"></span><span style="left:0;top:51px;width:28px"></span><span style="left:35px;top:51px;width:55px"></span><span style="left:0;top:66px;width:38px"></span></div>
  <div class="bars" style="left:661px"><span style="left:0;top:0;width:70px"></span><span style="left:0;top:17px;width:90px"></span><span style="left:0;top:34px;width:55px"></span><span style="left:0;top:51px;width:28px"></span><span style="left:35px;top:51px;width:55px"></span><span style="left:0;top:66px;width:38px"></span></div>
  <div class="bars" style="left:837px"><span style="left:0;top:0;width:70px"></span><span style="left:0;top:17px;width:90px"></span><span style="left:0;top:34px;width:55px"></span><span style="left:0;top:51px;width:28px"></span><span style="left:35px;top:51px;width:55px"></span><span style="left:0;top:66px;width:38px"></span></div>
</footer>

</body>
</html>
```